Construction Company Website Design

I need a Website Design for a Construction Company. I have attached logo and business card design files (a.i) to match styles and text for the website. I will need design for 3 pages:
1. A Home page
2. A secondary page (will be different information pages)
3. A contact page with submision form
Website to look professional and match the 'theme' across all pages, using main colours / reverse colours as per design files. Must be clear it is a construction related website without being over the top. Happy for the construction related details (whether that be images/outlines/backgrounds etc to be fairly subtle and not overbearing on the contect of the pages. It will be the content that will be most important, not the images within.

Content has not yet been fully completed but attached is a site map. Each page will need a space for the insertion of the relevant heading and associated content for that particular page. Example can be used as per attached map. If it is preferable to have content completed for this to be a more succesful project please advise and I will complete and submit.

Target Market(s)

Clients for potential construction projects. These could be a range of people. All would be very professional, well educated and put a substantial expection on the quality of website provided.

Industry/Entity Type

Construction

Number of Pages Required

3 page

Font styles to use
Serif
Sans Serif
Other font styles liked:
• fonts preferable as per design files provided unless designer beleives a different font would suit better

Requirements
Must have
• Colour scheme to match logo and business card files provided. Fonts that match as per provided files. Pages must be consistent with the theme carrying across all pages. All pages must have contact details at the bottom of the page.
• Contents of page 1 - 'Home page': multiple tab options / logo link
• Contents of page 2 - 'Secondary page': Top and side navigation / area for information and/or images.
• Contents of page - 'Contact us page': Top and side navigation / Submission form / area for logos such as linkdin, facebook etc.
Nice to have
• Would be good to have a or some generic construction related images - outlines / shadows / effects etc. These might be background images or outlines related to the relevant industry and are consistent across the pages. Could be outlines of buildings, images of men with hardhats etc etc. Good to see colour scheme as per design files used
Should not have
• No pictures of houses. Generally no photos. If any imagery of people must not show faces/details.

```html
<!DOCTYPE html>
<html lang="en">
<head>
<meta charset="utf-8">
<title>K.R.T Constructions</title>
<link href="https://fonts.googleapis.com/css2?family=Montserrat:wght@500;600;700&family=Roboto:ital,wght@0,400;0,500;0,700;1,400&display=swap" rel="stylesheet">
<style>
:root{
  --blue:#1ea7e4;
  --blue-dark:#0d8fcc;
  --ink:#1a1a1a;
  --grey-text:#555;
  --logo-grey:#6a6a6a;
  --panel:#efefef;
  --panel-2:#e9e9e9;
  --line:#dcdcdc;
  --line-blue:#9fe0f2;
  --night:#1e1f22;
  --white:#fff;
}
*{box-sizing:border-box;margin:0;padding:0}
html,body{width:1200px;height:2800px;overflow:hidden}
body{position:relative;font-family:"Roboto",sans-serif;color:var(--ink);background:var(--white)}
.abs{position:absolute}
section,header,nav,footer{position:absolute;left:0;width:1200px}

/* header */
.site-header{top:0;height:116px;background:linear-gradient(#fdfdfd,#e4e4e4)}
.site-header::before{content:"";position:absolute;left:0;top:0;width:100%;height:3px;background:var(--blue)}
.contact-tab{left:950px;top:0;width:100px;height:32px;background:var(--blue);color:#fff;font:700 13px "Roboto",sans-serif;display:flex;align-items:center;justify-content:center;clip-path:polygon(0 0,100% 0,92% 100%,8% 100%)}
.brand{left:140px;top:38px;font:600 30px "Montserrat",sans-serif;color:var(--logo-grey);letter-spacing:1px}
.brand small{font-size:20px;letter-spacing:1px;margin-left:12px}
.top-contact{top:58px;display:flex;align-items:center;gap:10px;font:400 17px "Roboto",sans-serif;color:#333}
.ico{width:26px;height:26px;border-radius:50%;background:var(--blue);display:flex;align-items:center;justify-content:center;flex:none}
.ico.square{border-radius:6px}
.search{left:870px;top:52px;width:190px;height:40px;border-radius:20px;background:#fff;box-shadow:inset 0 1px 3px rgba(0,0,0,.2);font:italic 400 13px "Roboto",sans-serif;color:#888;padding:12px 14px}
.search .btn{position:absolute;right:4px;top:5px;width:30px;height:30px;border-radius:50%;background:#555;display:flex;align-items:center;justify-content:center}

/* nav */
.main-nav{top:116px;height:56px;background:linear-gradient(#3a3a3a,#0c0c0c)}
.main-nav a{position:absolute;top:0;height:56px;line-height:58px;color:#fff;text-decoration:none;font:500 20px "Roboto",sans-serif;letter-spacing:1px}
.main-nav a.active{background:#e8e8e8;color:var(--blue);width:100px;text-align:center;left:140px}

/* hero */
.hero{top:172px;height:560px;overflow:hidden}
.hero-copy{left:140px;top:124px;color:#fff}
.hero-copy h1{font:600 27px/1.4 "Montserrat",sans-serif;letter-spacing:1px}
.hero-copy p{font:400 20px "Montserrat",sans-serif;letter-spacing:1px;margin-top:10px}
.hero-btn{left:226px;top:264px;width:200px;height:40px;border-radius:8px;background:#fff;color:var(--blue);font:500 17px "Roboto",sans-serif;letter-spacing:1px;display:flex;align-items:center;justify-content:center}
.dots{left:284px;top:336px;display:flex;gap:8px}
.dots i{width:12px;height:12px;border-radius:50%;background:#fff}
.dots i.on{background:#aaa}

/* section headings */
.heading{left:0;width:1200px;text-align:center;font:700 26px "Roboto",sans-serif;letter-spacing:2px;color:var(--ink)}
.heading em{font-style:normal;color:var(--blue)}
.rule{left:140px;width:920px;height:2px;background:var(--line)}
.rule.blue{background:var(--line-blue)}
.mini-mark{left:0;width:1200px;text-align:center;font:600 17px "Montserrat",sans-serif;color:var(--logo-grey);letter-spacing:1px}
.mini-mark span{background:inherit;padding:0 6px}

/* welcome */
.welcome{top:732px;height:416px;background:#fff}
.welcome .lead{left:220px;top:176px;width:760px;text-align:center;font:400 19px/1.62 "Roboto",sans-serif;color:#222;letter-spacing:.5px}
.pill{height:40px;border-radius:10px;background:var(--blue);color:#fff;font:700 17px "Roboto",sans-serif;letter-spacing:1px;display:flex;align-items:center;justify-content:center}

/* services */
.services{top:1148px;height:452px;background:var(--panel)}
.card{top:136px;width:200px;height:256px;background:#fff;overflow:hidden}
.card .photo{position:absolute;left:0;top:0;width:200px;height:200px}
.card .label{position:absolute;left:0;bottom:0;width:200px;height:84px;background:var(--blue);clip-path:polygon(0 20%,100% 0,100% 100%,0 100%);color:#fff;font:400 18px/1.55 "Roboto",sans-serif;text-align:center;display:flex;align-items:flex-end;justify-content:center;padding-bottom:6px;letter-spacing:.5px}
.slide-arrow{width:36px;height:36px;background:#999;display:flex;align-items:center;justify-content:center}

/* why */
.why{top:1600px;height:430px;background:#fff}
.reason{left:136px;display:flex;gap:20px}
.reason .ico{width:60px;height:60px}
.reason h3{font:700 18px "Roboto",sans-serif;margin-top:4px}
.reason p{font:400 13px/1.6 "Roboto",sans-serif;color:#222;margin-top:6px}

/* testimonial */
.testimonial{top:2030px;height:362px;background:var(--panel-2)}
.avatar{left:262px;top:150px;width:136px;height:136px;border-radius:50%;background:#fff;box-shadow:0 0 0 8px #dcdcdc}
.avatar div{position:absolute;left:10px;top:10px;width:116px;height:116px;border-radius:50%;background:linear-gradient(#cfd8df,#9fb3c2)}
.quote-text{left:426px;top:138px;width:520px;font:italic 400 15px/1.75 "Roboto",sans-serif;color:#444;letter-spacing:.5px}
.author{left:778px;top:246px;font:700 13px "Roboto",sans-serif;letter-spacing:2px;color:#444}
.author small{display:block;font-size:10px;margin-top:8px;margin-left:4px;letter-spacing:1.5px}
.qmark{font:700 110px/1 "Montserrat",sans-serif;color:#cfcfcf}

/* contact footer */
.contact{top:2392px;height:368px;background:linear-gradient(#2a2c30,#1a1b1e 60%,#272521)}
.contact .heading,.contact .mini-mark{color:#fff}
.contact .rule{background:#1ea7e4;opacity:.6}
.info{left:142px;display:flex;gap:18px;color:#fff}
.info h4{font:400 17px "Roboto",sans-serif;letter-spacing:1px}
.info p{font:400 13px/1.6 "Roboto",sans-serif;margin-top:8px}
.info p.big{font-size:20px;letter-spacing:2px;margin-top:6px}
.divider{left:438px;top:114px;width:1px;height:210px;background:#555}
.form-title{left:494px;top:112px;font:400 16px "Roboto",sans-serif;color:#fff;letter-spacing:1px}
.field{left:492px;width:264px;height:24px;border:1px solid #666;font:700 11px "Roboto",sans-serif;color:#fff;padding:5px 10px}
.message{left:784px;top:138px;width:270px;height:136px;border:1px solid #666;font:700 11px "Roboto",sans-serif;color:#fff;padding:8px 10px}
.big-mark{left:940px;top:92px;font:600 38px "Montserrat",sans-serif;color:#8a8a8a;letter-spacing:2px}
.submit{left:876px;top:294px;width:100px;height:24px;border-radius:8px;background:var(--blue);color:#fff;font:700 13px "Roboto",sans-serif;letter-spacing:1px;display:flex;align-items:center;justify-content:center}

.copyright{top:2760px;height:40px;background:#0b0b0b;color:#fff;font:700 12px "Roboto",sans-serif}
.copyright .left{left:142px;top:14px}
.follow{left:798px;top:8px;display:flex;align-items:center;gap:6px;font:700 14px "Roboto",sans-serif;letter-spacing:1px}
.follow i{width:26px;height:26px;background:var(--blue);display:block}
.follow b{margin-right:10px}
</style>
</head>
<body>

<header class="site-header">
  <div class="abs contact-tab">CONTACT</div>
  <div class="abs brand">K.R.T<small>CONSTRUCTIONS</small></div>
  <div class="abs top-contact" style="left:496px">
    <span class="ico square"><svg width="12" height="16" viewBox="0 0 12 16"><rect x="1" y="1" width="10" height="14" rx="2" fill="none" stroke="#fff" stroke-width="2"/></svg></span>(5550)148-2297
  </div>
  <div class="abs top-contact" style="left:682px">
    <span class="ico"><svg width="14" height="10" viewBox="0 0 14 10"><rect x="0" y="0" width="14" height="10" fill="#fff"/><path d="M0 0 7 6 14 0" fill="none" stroke="#1ea7e4" stroke-width="1.5"/></svg></span>hello@krtbuild.com
  </div>
  <div class="abs search">Search
    <span class="btn"><svg width="14" height="14" viewBox="0 0 14 14"><circle cx="6" cy="6" r="4" fill="none" stroke="#fff" stroke-width="2"/><path d="M9 9l4 4" stroke="#fff" stroke-width="2"/></svg></span>
  </div>
</header>

<nav class="main-nav">
  <a class="active" href="#">HOME</a>
  <a href="#" style="left:272px">ABOUT US</a>
  <a href="#" style="left:424px">SERVICE</a>
  <a href="#" style="left:556px">PROJECT</a>
  <a href="#" style="left:694px">CLIENT</a>
  <a href="#" style="left:816px">MEDIA</a>
  <a href="#" style="left:932px">CONTACT US</a>
</nav>

<section class="hero">
  <svg class="abs" style="left:0;top:0" width="1200" height="560" viewBox="0 0 1200 560">
    <defs>
      <linearGradient id="heroPhoto" x1="0" y1="0" x2="1" y2="1">
        <stop offset="0" stop-color="#9fb0bf"/>
        <stop offset=".6" stop-color="#7b8894"/>
        <stop offset="1" stop-color="#3c4248"/>
      </linearGradient>
      <linearGradient id="heroBlue" x1="0" y1="0" x2="1" y2="0">
        <stop offset="0" stop-color="#1c9fd9"/>
        <stop offset="1" stop-color="#22aee8"/>
      </linearGradient>
    </defs>
    <rect width="1200" height="560" fill="url(#heroBlue)"/>
    <path d="M1010 0 C 770 120 610 380 530 560 L1200 560 L1200 0 Z" fill="#dfe3e6"/>
    <g role="img" aria-label="Silhouette of a construction worker holding a torch against cranes and an evening sky">
      <path d="M1026 0 C 786 120 628 380 550 560 L1200 560 L1200 0 Z" fill="url(#heroPhoto)"/>
    </g>
  </svg>
  <div class="abs hero-copy">
    <h1>Lorem ipsum dolor sit amet<br>gloriatur contentiones</h1>
    <p>Ludus incorrupte in sit, ei quem fabellas</p>
  </div>
  <div class="abs hero-btn">REQUEST</div>
  <div class="abs dots"><i></i><i class="on"></i><i></i><i></i></div>
</section>

<section class="welcome">
  <div class="abs heading" style="top:72px;font-size:24px">WELCOME TO <span style="font:600 38px 'Montserrat',sans-serif;color:var(--logo-grey);margin-left:10px;vertical-align:-6px">K.R.T</span></div>
  <div class="abs rule" style="top:150px"></div>
  <div class="abs mini-mark" style="top:138px"><span style="background:#fff">K.R.T</span></div>
  <p class="abs lead">Lorem ipsum dolor sit amet, putent dissentias reformidans est id, vidit maiestatis mel ei. Mel aliquip partiendo et. Pro ut debet mnesarchum, duo percipit definitiones in. Duo iriure conclusionemque no, pri euismod eligendi id.</p>
  <div class="abs pill" style="left:522px;top:324px;width:154px">READ MORE</div>
</section>

<section class="services">
  <h2 class="abs heading" style="top:42px">OUR <em>SERVICE</em></h2>
  <div class="abs rule" style="top:106px"></div>
  <div class="abs mini-mark" style="top:94px"><span style="background:var(--panel)">K.R.T</span></div>
  <div class="abs slide-arrow" style="left:82px;top:248px"><svg width="12" height="16"><path d="M9 2 3 8l6 6" fill="none" stroke="#fff" stroke-width="2"/></svg></div>
  <div class="abs slide-arrow" style="left:1080px;top:248px"><svg width="12" height="16"><path d="M3 2l6 6-6 6" fill="none" stroke="#fff" stroke-width="2"/></svg></div>

  <div class="abs card" style="left:140px"><div class="photo" role="img" aria-label="Worker in hard hat and safety vest on site" style="background:linear-gradient(160deg,#6f7f8e,#3b4650 70%,#a9713a)"></div><div class="label">Lorem ipsum</div></div>
  <div class="abs card" style="left:380px"><div class="photo" role="img" aria-label="Team of workers in hard hats under a blue sky" style="background:linear-gradient(170deg,#9cc6ea,#6e8fae 60%,#3e4c5b)"></div><div class="label">Lorem ipsum Dolor</div></div>
  <div class="abs card" style="left:622px"><div class="photo" role="img" aria-label="Silhouette of worker with torch and crane" style="background:linear-gradient(170deg,#a7b6c4,#6d7986 60%,#2e3338)"></div><div class="label">Lorem ipsum Dolor<br>Sit Amet</div></div>
  <div class="abs card" style="left:858px"><div class="photo" role="img" aria-label="City skyline with construction cranes at dusk" style="background:linear-gradient(180deg,#c9b9a4,#8e8aa0 50%,#3f4c66)"></div><div class="label">Lorem ipsum Dolor<br>Sit Amet,Cu Ipsum</div></div>
</section>

<section class="why">
  <h2 class="abs heading" style="top:28px">WHY <em>CHOSE US</em></h2>
  <div class="abs rule blue" style="top:98px"></div>
  <div class="abs mini-mark" style="top:86px"><span style="background:#fff">K.R.T</span></div>

  <div class="abs reason" style="top:148px">
    <span class="ico"><svg width="28" height="30" viewBox="0 0 28 30"><circle cx="14" cy="11" r="9" fill="none" stroke="#fff" stroke-width="3"/><path d="M8 18 5 28l5-3 3 4M20 18l3 10-5-3-3 4" fill="none" stroke="#fff" stroke-width="2"/></svg></span>
    <div><h3>Lorem ipsum dolor sit amet</h3><p>eligendi ocurreret repudiare mei no,<br>natum similique mea cu, te discere vivendum sea</p></div>
  </div>
  <div class="abs reason" style="top:242px">
    <span class="ico"><svg width="28" height="28" viewBox="0 0 28 28"><rect x="3" y="5" width="22" height="20" rx="2" fill="none" stroke="#fff" stroke-width="2.5"/><path d="M3 11h22M9 2v6M19 2v6" stroke="#fff" stroke-width="2.5"/><path d="M9 18l3 3 6-6" fill="none" stroke="#fff" stroke-width="2"/></svg></span>
    <div><h3>Lorem ipsum dolor sit amet</h3><p>eligendi ocurreret repudiare mei no,<br>natum similique mea cu, te discere vivendum sea</p></div>
  </div>
  <div class="abs reason" style="top:336px">
    <span class="ico"><svg width="30" height="24" viewBox="0 0 30 24"><rect x="2" y="3" width="26" height="8" fill="none" stroke="#fff" stroke-width="2"/><path d="M6 11v10M24 11v10M9 3l4 8M17 3l4 8" stroke="#fff" stroke-width="2"/></svg></span>
    <div><h3>Lorem ipsum dolor sit amet</h3><p>eligendi ocurreret repudiare mei no,<br>natum similique mea cu, te discere vivendum sea</p></div>
  </div>

  <div class="abs" role="img" aria-label="Interior of a modern glass and steel building under construction" style="left:606px;top:140px;width:448px;height:262px;background:linear-gradient(135deg,#1b4f7a,#4f9ccd 45%,#cfe6f3 60%,#2a5d88)"></div>
</section>

<section class="testimonial">
  <h2 class="abs heading" style="top:20px">WHAT OUR <em>CUSTOMER US</em></h2>
  <div class="abs rule blue" style="top:72px"></div>
  <div class="abs mini-mark" style="top:60px"><span style="background:var(--panel-2)">K.R.T</span></div>
  <svg class="abs" style="left:84px;top:164px" width="36" height="64"><path d="M32 2 4 32l28 30" fill="none" stroke="#cfcfcf" stroke-width="4"/></svg>
  <svg class="abs" style="left:1078px;top:164px" width="36" height="64"><path d="M4 2l28 30-28 30" fill="none" stroke="#cfcfcf" stroke-width="4"/></svg>
  <div class="abs qmark" style="left:150px;top:152px">“</div>
  <div class="abs qmark" style="left:984px;top:152px">”</div>
  <div class="abs avatar"><div role="img" aria-label="Client portrait"></div></div>
  <p class="abs quote-text">Lorem ipsum dolor sit amet, eligendi ocurreret repudiare mei no, natum similique mea cu, te discere vivendum sea. Ius eu unum petentium deterruisset, nibh ridens inermis eu mel. Paulo simul aliquip pri te. Mutat accusamus dissentiet ad vis.</p>
  <div class="abs author">- MARCUS HALE<small>MARKETING MANAGER</small></div>
</section>

<footer class="contact">
  <div class="abs" role="img" aria-label="Darkened construction site at night" style="left:0;top:0;width:1200px;height:368px;background:linear-gradient(180deg,rgba(60,58,54,.35),rgba(20,20,22,.2) 50%,rgba(90,70,40,.25))"></div>
  <h2 class="abs heading" style="top:22px;color:#fff">CONTACT <em>US</em></h2>
  <div class="abs rule" style="top:70px"></div>
  <div class="abs mini-mark" style="top:64px;color:#777">K.R.T</div>

  <div class="abs info" style="top:110px">
    <span class="ico"><svg width="14" height="10"><rect width="14" height="10" fill="#fff"/><path d="M0 0 7 6 14 0" fill="none" stroke="#1ea7e4" stroke-width="1.5"/></svg></span>
    <div><h4>ADDRESS INFORMATION</h4><p>Harum offendit appellantur eos<br>no, eum sonet omnium in 1234</p></div>
  </div>
  <div class="abs info" style="top:192px">
    <span class="ico"><svg width="14" height="10"><rect width="14" height="10" fill="#fff"/><path d="M0 0 7 6 14 0" fill="none" stroke="#1ea7e4" stroke-width="1.5"/></svg></span>
    <div><h4>EMAIL</h4><p>hello@krtbuild.com</p></div>
  </div>
  <div class="abs info" style="top:272px">
    <span class="ico square"><svg width="12" height="16"><rect x="1" y="1" width="10" height="14" rx="2" fill="none" stroke="#fff" stroke-width="2"/></svg></span>
    <div><h4>CALL US</h4><p class="big">5550-716-4820</p></div>
  </div>

  <div class="abs divider"></div>
  <div class="abs form-title">LEAVES US MESSAGE</div>
  <div class="abs field" style="top:138px">Name</div>
  <div class="abs field" style="top:176px">Company</div>
  <div class="abs field" style="top:214px">Email</div>
  <div class="abs field" style="top:252px">Phone</div>
  <div class="abs field" style="top:290px">Zip</div>
  <div class="abs big-mark">K.R.T</div>
  <div class="abs message">Message</div>
  <div class="abs submit">SUBMIT</div>
</footer>

<div class="abs copyright" style="left:0;width:1200px">
  <div class="abs left">Copyright © 2018 KRT Contracting ALL RIGHT RESERVED</div>
  <div class="abs follow"><b>FOLLOW US :</b><i></i><i></i><i></i><i></i></div>
</div>

</body>
</html>
```